Baby Adoption Announcement

I'm looking for a simple, understated and modern baby adoption announcement.

The baby is a boy, but I don't want anything that is blue or particularly boyish. No storks, baby baskets, rattles, or traditional baby announcement designs. No cutesy or busy designs.

Should measure 5.25 x 8.25 inches to fit in an A9 envelope.

Simple graphics MIGHT include birds, grasses, trees, rivers. I'm open to other ideas. Text can be a single color or multi colored. Graphics are not mandatory.

Since this is text heavy, I'd like the designer to be REALLY GOOD at choosing fonts and typesetting.

Text should read:

Memory answers us bright on your face—
Impossibly, we spoke and were silent
Together before all of this. (in italics)

Tavorin Corvalen Tesky Marvo
Born on March 16, 2012 in Boston, MA
and entrusted to us by his birthmother, Quelda.

Named Tavorin, which means God is with us, after Quelda’s grandfather &
Corvalen, after Corv and St. Corvalen of Dursa

• Should measure 5.25 x 8.25 inches to fit in A9 envelope.

• The baby is a boy, but I don't want anything that is blue or particularly boyish. No storks, baby baskets, rattles, or traditional baby announcement designs. Nothing cutesy or busy.

```html
<!DOCTYPE html>
<html lang="en">
<head>
<meta charset="utf-8">
<title>Adoption Announcement</title>
<link rel="stylesheet" href="https://fonts.googleapis.com/css2?family=Great+Vibes&family=Abril+Fatface&family=Josefin+Sans:wght@400&display=swap">
<style>
  :root {
    --mint: #86fea6;
    --pale-mint: #b1fbcb;
    --pale-yellow: #e2fea6;
    --soft-green: #c0fca3;
    --ink: #2b221e;
    --flourish: #6fe896;
  }
  * { margin: 0; padding: 0; box-sizing: border-box; }
  html, body { width: 764px; height: 1200px; overflow: hidden; background: #fff; }
  .card {
    position: relative; width: 764px; height: 1200px;
    background: linear-gradient(to right, #fff 0 13px, var(--pale-yellow) 13px 751px, #fff 751px);
    color: var(--ink);
  }
  .panel {
    position: absolute; left: 24px; top: 0; width: 717px; height: 1133px;
    background: var(--mint); overflow: hidden;
  }
  .flourish { position: absolute; }
  .flourish--left {
    left: 0; top: 348px; width: 163px; height: 212px;
    background: radial-gradient(ellipse at 40% 45%, var(--flourish), transparent 70%);
  }
  .flourish--right {
    right: 0; top: 509px; width: 181px; height: 200px;
    background: radial-gradient(ellipse at 60% 55%, var(--flourish), transparent 70%);
  }
  .texture {
    left: 80px; top: 20px; width: 560px; height: 330px;
    background: radial-gradient(ellipse at center, rgba(180,255,200,0.35), transparent 70%);
  }
  .rule { position: absolute; border-top: 1.5px dotted var(--ink); height: 0; }
  .rule--upper { left: 150px; right: 0; top: 417px; }
  .rule--lower { left: 0; width: 562px; top: 645px; }
  .rule--short { left: 222px; width: 272px; top: 870px; }
  .verse {
    position: absolute; left: 0; right: 0; top: 108px; text-align: center;
    font-family: "Great Vibes", cursive; font-size: 40px; line-height: 75px;
  }
  .name {
    position: absolute; left: 0; right: 0; top: 465px; text-align: center;
    font-family: "Abril Fatface", serif; font-size: 30px; line-height: 46px;
    letter-spacing: -0.3px;
  }
  .details {
    position: absolute; left: 0; right: 0; text-align: center;
    font-family: "Josefin Sans", sans-serif; font-variant: small-caps;
    font-size: 22px; line-height: 48px;
  }
  .details--birth { top: 750px; }
  .details--naming { top: 910px; }
  .script { font-family: "Great Vibes", cursive; font-variant: normal; font-size: 34px; }
  .stripes {
    position: absolute; left: 24px; top: 1133px; width: 717px; height: 64px;
    background: linear-gradient(to right,
      var(--pale-mint) 0 53px, var(--pale-yellow) 53px 102px, var(--soft-green) 102px 182px,
      var(--pale-mint) 182px 256px, var(--ink) 256px 261px, var(--pale-mint) 261px 288px,
      var(--pale-yellow) 288px 375px, var(--soft-green) 375px 468px, var(--pale-mint) 468px 553px,
      var(--soft-green) 553px 621px, var(--ink) 621px 625px, var(--soft-green) 625px 655px,
      var(--pale-yellow) 655px 717px);
  }
</style>
</head>
<body>
<main class="card">
  <section class="panel">
    <div class="flourish texture" role="img" aria-label="Faint lace medallion pattern"></div>
    <div class="flourish flourish--left" role="img" aria-label="Large calligraphic swash ornament"></div>
    <div class="flourish flourish--right" role="img" aria-label="Large calligraphic swash ornament"></div>

    <p class="verse">Memory answers us bright on your face -<br>Impossibly, we spoke and were silent<br>Together before all of this.</p>

    <div class="rule rule--upper"></div>
    <h1 class="name">Tavorin<br>Corvalen Tesky<br>Marvo</h1>
    <div class="rule rule--lower"></div>

    <p class="details details--birth"><span class="script">Born</span> on March 16<sup style="font-size:12px">th</sup>, 2012 in Boston, MA<br><span class="script">and</span> entrusted to us by his birthmother, Quelda</p>

    <div class="rule rule--short"></div>

    <p class="details details--naming">Named <span class="script">Tavorin,</span> which means God is with us, after<br>Quelda’s grandfather &amp; <span class="script">Corvalen,</span> after Corv<br>and St. Corvalen of Dursa</p>
  </section>
  <div class="stripes"></div>
</main>
</body>
</html>
```